Einladungskarte
Zielgruppe
Hochzeitsgäste zwischen 30 und 40
Aufgabenstellung
Die Einladung hat folgende Eckdaten:
- Format Din A5 (Doppelseitiger DinA 4 gefalzt) Einladungsbogen (wird leichter Karton)
- Zusätzlicher Einlagebogen für Einladungstext
- Stil klassisch/elegant eher schlicht aber jung
- Grundthema Gerberablume (weiß, beige, rot oder orange)
- Hintergrund (hell)
- Zusätzlich zur Einladung wird Bildrecht der Blume für ein Banner auf der Hochzeitswebseite benötigt
- Editierbare Graphikdatei wird benötigt (da der Text der Einladung noch nicht final ist)

```html
<!DOCTYPE html>
<html lang="de">
<head>
<meta charset="utf-8">
<title>Einladung zur Hochzeit</title>
<link rel="stylesheet" href="https://fonts.googleapis.com/css2?family=Marcellus&display=swap">
<style>
  :root {
    --page-bg: #f3f2f0;
    --card-bg: #ffffff;
    --heading-orange: #cf5a19;
    --names-gold: #e6b12c;
    --petal-orange: #e8661c;
    --petal-yellow: #f2a62a;
    --stem-green: #7c8a3c;
    --bottom-band: #f0c044;
  }
  html, body {
    margin: 0;
    padding: 0;
    width: 1200px;
    height: 845px;
    overflow: hidden;
    background: var(--page-bg);
  }
  .canvas {
    position: relative;
    width: 1200px;
    height: 845px;
  }
  .invitation-card {
    position: absolute;
    left: 324px;
    top: 32px;
    width: 552px;
    height: 780px;
    background: var(--card-bg);
    overflow: hidden;
  }
  .card-title {
    position: absolute;
    top: 116px;
    left: 0;
    width: 100%;
    margin: 0;
    text-align: center;
    font-family: "Marcellus", "Optima", serif;
    font-weight: 400;
  }
  .card-title__main {
    display: block;
    font-size: 74px;
    line-height: 1;
    font-variant: small-caps;
    letter-spacing: 2px;
    color: var(--heading-orange);
  }
  .card-title__sub,
  .card-title__names {
    display: block;
    font-size: 33px;
    line-height: 1.2;
    font-variant: small-caps;
    letter-spacing: 1px;
    color: var(--names-gold);
  }
  .card-title__sub { margin-top: 6px; }
  .flower-photo {
    position: absolute;
    left: 0;
    top: 330px;
    width: 552px;
    height: 428px;
    display: block;
  }
  .bottom-band {
    position: absolute;
    left: 0;
    bottom: 0;
    width: 100%;
    height: 22px;
    background: var(--bottom-band);
  }
</style>
</head>
<body>
<main class="canvas">
  <section class="invitation-card">
    <h1 class="card-title">
      <span class="card-title__main">Einladung</span>
      <span class="card-title__sub">zur Hochzeit von</span>
      <span class="card-title__names">Marlene &amp; Jonas</span>
    </h1>

    <svg class="flower-photo" viewBox="0 0 552 428" role="img" aria-label="Nahaufnahme einer orangefarbenen Gerberablüte mit feinen grünen Gräsern, die nach oben in Weiß ausblendet">
      <defs>
        <linearGradient id="photoFade" x1="0" y1="0" x2="0" y2="1">
          <stop offset="0" stop-color="#ffffff"/>
          <stop offset="0.25" stop-color="#f9e3cf"/>
          <stop offset="0.55" stop-color="#ee9a45"/>
          <stop offset="0.85" stop-color="#d9661f"/>
          <stop offset="1" stop-color="#8a8a3e"/>
        </linearGradient>
        <linearGradient id="sideFade" x1="0" y1="0" x2="1" y2="0">
          <stop offset="0" stop-color="#ffffff" stop-opacity="0"/>
          <stop offset="0.7" stop-color="#ffffff" stop-opacity="0"/>
          <stop offset="1" stop-color="#ffffff" stop-opacity="0.55"/>
        </linearGradient>
      </defs>
      <rect width="552" height="428" fill="url(#photoFade)"/>
      <rect width="552" height="428" fill="url(#sideFade)"/>
    </svg>

    <div class="bottom-band"></div>
  </section>
</main>
</body>
</html>
```